Price list for young Relaxon clinic

I require a price list/Treatment menu for clinic

To include:
Logo
Address
Phone number
Website

List of services and Prices
Relaxon 1 area £100
Relaxon 2 areas £150
Relaxon 3 areas £200
Lip Enhancement 0.5ml £100
Lip Enhancement 1ml £200
Facial Fillers £200 per 1ml
Volumiq £450 per session (2 vials - must be bought as a course)
Non Surgical Face Lift (Thread Lift) £600 per area
Skin Press Full Face £250
Skin Press Small Per Small Area £100
Cryo Therapy £60
Chemical Peel Light Peel and Microdermabrasion £85
Chemical Peel Deep Peel £150
Consultation £30 redeemable against service
Relaxon Top Up Relaxon £50 (must be within 2 weeks of 1st treatment)
Filler Top Up £100 (must be within 2 weeks of 1st appointment)

Open Hours
Updates

Company Name: HVM Address: 482 Pellbrook Road, 6 Warnford High Street, KT4 3JQ Phone: 0208 947 2186 Website: www.hollyvanmereaesthetics.co.uk

Please add more colour

Needs to be much cleaner and simpler Front page to include logo and price list Back page to inculde open hours and contact information including google map. Please no images with needles. Images of lips and faces are good, but try not to crowd copy on the pagei. No copy on top of images. White, grey, black and reds are good on colouring.

Target Market(s)

young market ages 22-45 years old mainly female
modern

Industry/Entity Type

Clinic

Number of Pages Required

4 page

Requirements
Must have
• Logo - logo must be in colour grey/silver
• Address (small map?)
• Phone number
• Web address
• Services
• Open hours
• Prices
• Images

```html
<!DOCTYPE html>
<html lang="en">
<head>
<meta charset="utf-8">
<title>Holly Vanmere Aesthetics – Treatment Menu</title>
<link rel="stylesheet" href="https://fonts.googleapis.com/css2?family=EB+Garamond:wght@400&family=Marcellus+SC&display=swap">
<style>
  :root {
    --brand-blue: #1e9ad6;
    --brand-blue-deep: #17688f;
    --ink-teal: #1b9dd3;
    --logo-grey: #9a9a9a;
    --ink-dark: #2b2b2b;
    --paper: #ffffff;
    --charcoal: #2e3236;
  }
  * { margin: 0; padding: 0; box-sizing: border-box; }
  html, body { width: 885px; height: 1200px; overflow: hidden; background: var(--paper); }
  .menu { position: relative; width: 885px; height: 1200px; background: var(--paper); overflow: hidden; }

  .hero-photo { position: absolute; left: 0; top: 0; width: 368px; height: 520px;
    background: linear-gradient(180deg, #f4ece6 0%, #e9d3c4 55%, #dcbba6 100%); }
  .side-band { position: absolute; left: 0; top: 0; width: 385px; height: 1100px; }

  .about { position: absolute; left: 68px; top: 534px; width: 250px;
    font-family: "EB Garamond", serif; font-size: 16.5px; line-height: 22.5px; color: var(--paper); }
  .about p { margin-bottom: 18px; }

  .visit { position: absolute; left: 68px; top: 852px; width: 290px;
    font-family: "EB Garamond", serif; font-size: 14px; line-height: 18px; color: var(--paper); }
  .visit-title { font-family: "Marcellus SC", serif; font-size: 15px; }

  .location-map { position: absolute; left: 36px; top: 956px; width: 339px; height: 122px;
    background: linear-gradient(135deg, #eceae4, #dcdad3); }
  .map-pin { position: absolute; left: 162px; top: 40px; }

  .price-panel { position: absolute; left: 405px; top: 0; width: 445px; height: 1100px; background: var(--paper);
    box-shadow: 4px 0 8px rgba(0,0,0,.12); }
  .edge-strip { position: absolute; left: 850px; top: 360px; width: 35px; height: 740px; background: var(--brand-blue); }
  .edge-strip-dark { position: absolute; left: 850px; top: 778px; width: 35px; height: 62px; background: var(--charcoal); }

  .brand { position: absolute; left: 405px; top: 62px; width: 440px; display: flex; justify-content: center; align-items: center; gap: 14px; }
  .brand-dot { width: 34px; height: 34px; border-radius: 50%; background: var(--logo-grey); flex: none; }
  .brand-name { font-family: "EB Garamond", serif; font-size: 26px; line-height: 30px; letter-spacing: 4px;
    color: var(--logo-grey); text-transform: uppercase; }

  .price-row { position: absolute; left: 405px; width: 369px; text-align: right;
    font-family: "Marcellus SC", serif; color: var(--ink-teal); font-size: 21px; line-height: 22px; }
  .price-row small { font-size: 15px; }
  .price-note { position: absolute; left: 405px; width: 369px; text-align: right;
    font-family: "Marcellus SC", serif; color: var(--ink-teal); font-size: 15px; line-height: 18px; }
  .price { position: absolute; left: 786px; font-family: "EB Garamond", serif; font-size: 17px; color: var(--ink-dark); line-height: 22px; }

  .result-photo { position: absolute; top: 824px; width: 108px; height: 80px;
    background: linear-gradient(135deg, #e6cdbd, #c9a28c); }
  .progress-strip { position: absolute; left: 454px; top: 914px; width: 343px; height: 178px; }
  .progress-labels { display: flex; height: 16px; background: #8e8e8e; }
  .progress-labels span { flex: 1; font-family: Arial, sans-serif; font-size: 9px; color: #fff; text-align: center; line-height: 16px;
    border-right: 1px solid #fff; }
  .progress-labels span:last-child { border-right: 0; }
  .progress-photo { height: 162px; background: linear-gradient(180deg, #6e4a34, #a7714f 55%, #8a5a3e); }

  .contact { position: absolute; left: 0; top: 1100px; width: 885px; height: 100px; background: var(--paper); text-align: center; color: var(--ink-dark); }
  .contact-title { margin-top: 8px; font-family: "Marcellus SC", serif; font-size: 21px; line-height: 24px; }
  .contact-lines { font-family: "Marcellus SC", serif; font-size: 13px; line-height: 16px; }
  .contact-details { margin-top: 10px; font-family: "EB Garamond", serif; font-size: 17px; }
</style>
</head>
<body>
<main class="menu">
  <div class="hero-photo" role="img" aria-label="Close-up portrait of a woman's face"></div>

  <svg class="side-band" viewBox="0 0 385 1100" aria-hidden="true">
    <path d="M0 500 C90 470 200 440 368 450 L368 1100 L0 1100 Z" fill="var(--brand-blue)"/>
    <path d="M0 620 C80 570 170 580 230 640 L385 820 L385 1100 L0 1100 Z" fill="var(--brand-blue-deep)" opacity=".55"/>
  </svg>

  <section class="about">
    <p>Holly is a registered nurse and independent nurse prescriber with over 7 years experience in cosmetic medicine and facial injections.</p>
    <p>She is a member of the BSCN, NRC and insured with Harlow and Finch. She has worked with top plastic surgeons and dermatologists in NZ, Australia and the UK including Marlow Street.</p>
    <p>Holly will help you look your best and achieve a fresh and beautiful you.</p>
  </section>

  <section class="visit">
    <div class="visit-title">Open Hours</div>
    <div>Mon – Fri 10am – 7pm &nbsp;·&nbsp; Sat 10am – 4pm</div>
    <div>482 Pellbrook Road, 6 Warnford High Street, KT4 3JQ</div>
  </section>

  <div class="location-map" role="img" aria-label="Street map of the clinic location at Warnford High Street">
    <svg class="map-pin" width="16" height="26" viewBox="0 0 16 26" aria-hidden="true">
      <path d="M8 0 C3.6 0 0 3.6 0 8 C0 14 8 26 8 26 C8 26 16 14 16 8 C16 3.6 12.4 0 8 0 Z" fill="#d93a2b"/>
      <circle cx="8" cy="8" r="3" fill="#8c1d14"/>
    </svg>
  </div>

  <div class="price-panel"></div>
  <div class="edge-strip"></div>
  <div class="edge-strip-dark"></div>

  <header class="brand">
    <span class="brand-dot" aria-hidden="true"></span>
    <div class="brand-name">Holly Vanmere<br>Aesthetics</div>
  </header>

  <div class="price-row" style="top:198px">Relaxon <small>1 area</small></div><div class="price" style="top:198px">£100</div>
  <div class="price-row" style="top:222px">Relaxon <small>2 areas</small></div><div class="price" style="top:222px">£150</div>
  <div class="price-row" style="top:246px">Relaxon <small>3 areas</small></div><div class="price" style="top:246px">£200</div>

  <div class="price-row" style="top:290px">Lip Enhancement <small>0.5ml</small></div><div class="price" style="top:290px">£100</div>
  <div class="price-row" style="top:314px">Lip Enhancement <small>1 ml</small></div><div class="price" style="top:314px">£200</div>

  <div class="price-row" style="top:358px">Facial Fillers <small>per 1 ml</small></div><div class="price" style="top:358px">£200</div>
  <div class="price-row" style="top:382px">Volumiq <small>per session (2 vials -</small></div><div class="price" style="top:382px">£450</div>
  <div class="price-note" style="top:405px">must be bought as a course)</div>

  <div class="price-row" style="top:444px">Non Surgical Face Lift</div><div class="price" style="top:442px">£600</div>
  <div class="price-note" style="top:467px">(Thread Lift) per area</div>
  <div class="price-row" style="top:487px">Skin Press Full Face</div><div class="price" style="top:486px">£250</div>
  <div class="price-row" style="top:511px">Skin Press <small>Small Per Small</small></div><div class="price" style="top:509px">£100</div>
  <div class="price-note" style="top:533px">Area</div>
  <div class="price-row" style="top:555px">Cryo Therapy</div><div class="price" style="top:554px">£60</div>
  <div class="price-row" style="top:579px">Chemical Peel <small>Light Peel and</small></div><div class="price" style="top:577px">£85</div>
  <div class="price-note" style="top:602px">Microdermabrasion</div>
  <div class="price-row" style="top:623px">Chemical Peel <small>Deep Peel</small></div><div class="price" style="top:622px">£150</div>

  <div class="price-row" style="top:672px">Consultation <small>redeemable</small></div><div class="price" style="top:671px">£30</div>
  <div class="price-note" style="top:694px">against service</div>
  <div class="price-row" style="top:716px">Relaxon Top Up Relaxon <small>(must be</small></div><div class="price" style="top:715px">£50</div>
  <div class="price-note" style="top:738px">within 2 weeks of 1st treatment)</div>
  <div class="price-row" style="top:762px">Filler Top Up <small>(must be</small></div><div class="price" style="top:761px">£100</div>
  <div class="price-note" style="top:784px">within 2 weeks of 1st appointment)</div>

  <div class="result-photo" style="left:454px" role="img" aria-label="Before and after comparison of a woman's face"></div>
  <div class="result-photo" style="left:571px" role="img" aria-label="Before and after comparison of eye area"></div>
  <div class="result-photo" style="left:689px" role="img" aria-label="Before and after comparison of brow area"></div>

  <div class="progress-strip">
    <div class="progress-labels"><span>BEFORE</span><span>DAY 7</span><span>DAY 90</span><span>DAY 120</span></div>
    <div class="progress-photo" role="img" aria-label="Treatment progress series of a woman's forehead from before to day 120"></div>
  </div>

  <footer class="contact">
    <div class="contact-title">Contact us today</div>
    <div class="contact-lines">to book a cosmetic surgery consultation with Mr Owen Tarrick<br>(voted one of Glossline 2015's top plastic surgeons).</div>
    <div class="contact-details">Phone: 0208 947 2186 &nbsp;|Email: hvmwarnfordbookings@mailbox.com &nbsp;|www.hollyvanmereaesthetics.co.uk</div>
  </footer>
</main>
</body>
</html>
```